Wine Label Redesign For California Wine Company

We’re looking to refresh our brand with a new professional looking label. We love what we have and was well received over the past three years and would like to keep a couple of the element: Name (Marco Vellin), it doesn’t have to be in cursive. The swirl, this how everybody recognizes our brand as it’s also in our logo. Colors: Gold and whatever you think is awesome. Looking forward to seeing your work.

Target Market(s)

Retailers

Industry/Entity Type

Winery

Font styles to use
Serif
Script

Colors

Designer to choose colors to be used in the design.

Requirements
Must have
• Front Label:
• Symphony (Varietal)
• 2016 (vintage)
• Lodi, California (location)
• Marco Vellin (Name)
• Back Label:
• Government Warning
• www.vellinwineco-example.com (website)
• 2016 (vintage)
• Swirl
Nice to have
• Creativity
• Bold colors
• Something that pops
Should not have
• Should not look nothing like my old label.

```html
<!DOCTYPE html>
<html lang="en">
<head>
<meta charset="utf-8">
<title>Marco Vellin – Wine Labels</title>
<link rel="stylesheet" href="https://fonts.googleapis.com/css2?family=Oranienbaum&family=Cormorant+SC:wght@600;700&family=Cormorant:wght@600;700&display=swap">
<style>
  :root {
    --bg: #ffffff;
    --gold: #c0955c;
    --gold-light: #d8b373;
    --ink-black: #231f20;
    --wine-red: #9b1f22;
    --paper: #ffffff;
  }
  html, body { margin: 0; padding: 0; overflow: hidden; background: var(--bg); }
  .canvas { display: block; width: 1200px; height: 1000px; }
  .label-border { stroke-linejoin: round; stroke-width: 20; }
  .label-body { stroke: var(--paper); stroke-width: 7; stroke-linejoin: round; }
  .label--malbec .label-border { fill: var(--gold); stroke: var(--gold); }
  .label--malbec .label-body { fill: var(--ink-black); }
  .label--cabernet .label-border { fill: var(--gold-light); stroke: var(--gold-light); }
  .label--cabernet .label-body { fill: var(--wine-red); }
  .label--malbec .accent { fill: var(--gold); stroke: var(--gold); }
  .label--cabernet .accent { fill: var(--gold-light); stroke: var(--gold-light); }
  .rule { fill: none; stroke-width: 3; stroke-linecap: round; }
  .year-bar { stroke-width: 3; stroke-linecap: round; }
  .winery-name { font-family: "Oranienbaum", "Times New Roman", serif; font-size: 118px; fill: var(--paper); }
  .vintage { font-family: "Cormorant", Georgia, serif; font-weight: 700; font-size: 27px; fill: var(--paper); }
  .varietal { font-family: "Cormorant SC", Georgia, serif; font-weight: 700; font-size: 27px; letter-spacing: 1.5px; fill: var(--paper); }
  .origin { font-family: "Cormorant", Georgia, serif; font-weight: 600; font-size: 17px; letter-spacing: 1px; fill: var(--paper); }
</style>
</head>
<body>
<svg class="canvas" viewBox="0 0 1200 1000" xmlns="http://www.w3.org/2000/svg">
  <defs>
    <polygon id="badge-shape" points="850,70 1100,150 1100,188 1132,200 1132,393 850,510 568,393 568,200 600,188 600,150"/>
  </defs>

  <g class="label label--malbec">
    <use href="#badge-shape" class="label-border"/>
    <use href="#badge-shape" class="label-body"/>
    <g class="vintage-row">
      <line class="year-bar accent" x1="697" y1="162" x2="787" y2="162"/>
      <line class="year-bar accent" x1="697" y1="204" x2="787" y2="204"/>
      <line class="year-bar accent" x1="917" y1="162" x2="1007" y2="162"/>
      <line class="year-bar accent" x1="917" y1="204" x2="1007" y2="204"/>
      <text class="vintage" x="742" y="193" text-anchor="middle">20</text>
      <text class="vintage" x="962" y="193" text-anchor="middle">18</text>
    </g>
    <circle class="accent" cx="850" cy="178" r="24" role="img" aria-label="Brand swirl emblem"/>
    <text class="winery-name" x="850" y="331" text-anchor="middle" textLength="486" lengthAdjust="spacingAndGlyphs">MARCO VELLIN</text>
    <path class="rule accent" d="M683,356 Q850,344 1020,356"/>
    <text class="varietal" x="850" y="385" text-anchor="middle">Malbec Wine</text>
    <path class="rule accent" d="M683,404 Q850,392 1020,404"/>
    <polygon class="accent" points="843,399 857,399 850,405"/>
    <text class="origin" x="850" y="440" text-anchor="middle">• Lodi - California •</text>
  </g>

  <g class="label label--cabernet" transform="translate(-475 422)">
    <use href="#badge-shape" class="label-border"/>
    <use href="#badge-shape" class="label-body"/>
    <g class="vintage-row">
      <line class="year-bar accent" x1="697" y1="162" x2="787" y2="162"/>
      <line class="year-bar accent" x1="697" y1="204" x2="787" y2="204"/>
      <line class="year-bar accent" x1="917" y1="162" x2="1007" y2="162"/>
      <line class="year-bar accent" x1="917" y1="204" x2="1007" y2="204"/>
      <text class="vintage" x="742" y="193" text-anchor="middle">20</text>
      <text class="vintage" x="962" y="193" text-anchor="middle">18</text>
    </g>
    <circle class="accent" cx="850" cy="178" r="24" role="img" aria-label="Brand swirl emblem"/>
    <text class="winery-name" x="850" y="331" text-anchor="middle" textLength="486" lengthAdjust="spacingAndGlyphs">MARCO VELLIN</text>
    <path class="rule accent" d="M683,356 Q850,344 1020,356"/>
    <text class="varietal" x="850" y="385" text-anchor="middle">Cabernet Sauvignon</text>
    <path class="rule accent" d="M683,404 Q850,392 1020,404"/>
    <polygon class="accent" points="843,399 857,399 850,405"/>
    <text class="origin" x="850" y="445" text-anchor="middle">• Lodi - California •</text>
  </g>
</svg>
</body>
</html>
```